Pre-Paid Card for Teens needs a design

We are a Fintech company called Zorvella. We will sell prepaid cards for families and teens. Now we need a prepaid card design. Prepaid card should have a plexicard logo, company logo, 16 card number, expire date. Our webpage is http://www.zorvella-example.com
Target Market(s)
Teenages between 8 - 18 years old
Industry/Entity Type
It Company
Requirements
Must have
- The prepaid card must include zorvella logo, plexicard debit card logo (I already attached a sample card), 16 digit card number and expire date.
Nice to have
- It should be fun and prestigious for young people.
Should not have
- We don't want that the card has a lots of color

```html
<!DOCTYPE html>
<html lang="en">
<head>
<meta charset="utf-8">
<title>Zorvella Prepaid Card – Flat Previews</title>
<link rel="stylesheet" href="https://fonts.googleapis.com/css2?family=Jost:wght@300;400;600;700&family=Orbitron:wght@500;700&display=swap">
<style>
  :root {
    --page-bg: #ffffff;
    --card-base: #0e0846;
    --card-band: #1f1766;
    --card-edge: #15103a;
    --card-glow: #4b3f9c;
    --accent-yellow: #ffc20e;
    --accent-orange: #f29424;
    --label-rust: #c4561e;
    --scheme-red: #e8341c;
    --scheme-text: #ffffff;
    --title-ink: #15123f;
  }
  * { margin: 0; padding: 0; box-sizing: border-box; }
  html, body {
    width: 1200px; height: 798px; overflow: hidden;
    background: var(--page-bg);
  }
  .sheet { position: relative; width: 1200px; height: 798px; }

  .card {
    position: absolute;
    width: 496px; height: 312px;
    border-radius: 14px;
    overflow: hidden;
    background: var(--card-base);
  }
  .card--one { left: 40px; top: 42px; }
  .card--two { left: 638px; top: 42px; }
  .card--three { left: 40px; top: 440px; }

  .card__gloss { position: absolute; inset: 0; width: 100%; height: 100%; }

  .card__brand {
    position: absolute; left: 21px; top: 10px;
    font-family: "Jost", sans-serif; font-weight: 700;
    font-size: 42px; letter-spacing: 0.5px;
    color: var(--accent-orange);
  }
  .card__number {
    position: absolute; left: 22px; top: 240px;
    font-family: "Orbitron", sans-serif; font-weight: 700;
    font-size: 17px; letter-spacing: 1px;
    color: var(--accent-yellow);
  }
  .card__expiry {
    position: absolute; left: 22px; top: 272px;
    font-family: "Orbitron", sans-serif; font-weight: 500;
    font-size: 17px; color: var(--accent-yellow);
  }
  .card__expiry-label {
    font-family: "Jost", sans-serif; font-weight: 300;
    letter-spacing: 1.5px; color: var(--label-rust);
    margin-right: 6px;
  }
  .card__scheme {
    position: absolute; right: 20px; top: 236px;
    display: flex; align-items: center; gap: 8px;
  }
  .card__scheme-dot {
    width: 54px; height: 54px; border-radius: 50%;
    background: var(--scheme-red);
  }
  .card__scheme-name {
    font-family: "Jost", sans-serif; font-weight: 600;
    font-size: 20px; color: var(--scheme-text);
  }

  .title {
    position: absolute; left: 674px; top: 512px;
    font-family: "Jost", sans-serif; font-weight: 400;
    font-size: 52px; line-height: 76px;
    letter-spacing: 26px; color: var(--title-ink);
  }
</style>
</head>
<body>
<main class="sheet">

  <article class="card card--one">
    <svg class="card__gloss" viewBox="0 0 496 312" preserveAspectRatio="none" aria-hidden="true">
      <defs>
        <linearGradient id="band-a" x1="0" y1="0" x2="1" y2="0">
          <stop offset="0" stop-color="var(--card-band)"/>
          <stop offset="1" stop-color="var(--card-edge)"/>
        </linearGradient>
      </defs>
      <path d="M0 0 H496 V58 Q250 130 0 135 Z" fill="url(#band-a)"/>
    </svg>
    <div class="card__brand">zorvella</div>
    <div class="card__number">0000 0000 1234 5678</div>
    <div class="card__expiry"><span class="card__expiry-label">EXPIRES</span>00/XX</div>
    <div class="card__scheme"><span class="card__scheme-dot"></span><span class="card__scheme-name">plexicard</span></div>
  </article>

  <article class="card card--two">
    <svg class="card__gloss" viewBox="0 0 496 312" preserveAspectRatio="none" aria-hidden="true">
      <defs>
        <linearGradient id="body-b" x1="0" y1="0" x2="1" y2="0">
          <stop offset="0.45" stop-color="var(--card-base)"/>
          <stop offset="1" stop-color="var(--card-glow)"/>
        </linearGradient>
        <linearGradient id="band-b" x1="0" y1="0" x2="1" y2="0">
          <stop offset="0" stop-color="var(--card-band)"/>
          <stop offset="1" stop-color="#3d3470"/>
        </linearGradient>
      </defs>
      <rect width="496" height="312" fill="url(#body-b)"/>
      <path d="M0 0 H496 V58 Q250 130 0 135 Z" fill="url(#band-b)"/>
    </svg>
    <div class="card__brand">zorvella</div>
    <div class="card__number">0000 0000 1234 5678</div>
    <div class="card__expiry"><span class="card__expiry-label">EXPIRES</span>00/XX</div>
    <div class="card__scheme"><span class="card__scheme-dot"></span><span class="card__scheme-name">plexicard</span></div>
  </article>

  <article class="card card--three">
    <svg class="card__gloss" viewBox="0 0 496 312" preserveAspectRatio="none" aria-hidden="true">
      <defs>
        <linearGradient id="band-c" x1="0" y1="0" x2="1" y2="0">
          <stop offset="0" stop-color="var(--card-band)"/>
          <stop offset="1" stop-color="var(--card-edge)"/>
        </linearGradient>
      </defs>
      <path d="M0 0 H496 V58 Q250 130 0 135 Z" fill="url(#band-c)"/>
    </svg>
    <div class="card__brand">zorvella</div>
    <div class="card__number">0000 0000 1234 5678</div>
    <div class="card__expiry"><span class="card__expiry-label">EXPIRES</span>00/XX</div>
    <div class="card__scheme"><span class="card__scheme-dot"></span><span class="card__scheme-name">plexicard</span></div>
  </article>

  <h1 class="title">FLAT<br>PREVIEWS</h1>

</main>
</body>
</html>
```